Business Card Design - Cryotherapy

We need a custom created business card for our company FrostLeaf Spa. We provide whole body cryotherapy and localized cryotherapy to our clients. Please be creative.
Please see our website for idea's on design.
www.frostleafspa-example.com
Industry/Entity Type
Business
Contact Information for Business Card
Name, Position, Phone Number, Address, Website, Email
Look and feel
Each slider illustrates characteristics of the customer's brand and the style your logo design should communicate.

```html
<!DOCTYPE html>
<html lang="en">
<head>
<meta charset="utf-8">
<title>FrostLeaf Spa – Business Card</title>
<link href="https://fonts.googleapis.com/css2?family=Roboto:wght@400;500;700&display=swap" rel="stylesheet">
<style>
  :root {
    --backdrop: #a9a7a8;
    --card: #3b393b;
    --ink: #ffffff;
    --name-grey: #b9b9b9;
    --icon-grey: #bdbdbd;
    --band-teal: #1ba3ad;
    --band-green: #3f9a5c;
  }
  * { box-sizing: border-box; margin: 0; padding: 0; }
  html, body { width: 1200px; height: 1200px; overflow: hidden; }
  body {
    background: var(--backdrop);
    font-family: "Roboto", Arial, sans-serif;
    color: var(--ink);
    position: relative;
  }
  .card {
    position: absolute;
    left: 238px;
    width: 712px;
    height: 420px;
    background: var(--card);
    border-radius: 22px;
    overflow: hidden;
  }
  .card--front { top: 118px; }
  .card--back { top: 655px; }

  .wordmark {
    position: absolute;
    display: flex;
    align-items: center;
    gap: 12px;
    font-weight: 500;
    letter-spacing: 1px;
    color: var(--ink);
    white-space: nowrap;
  }
  .wordmark__dot {
    width: 16px; height: 16px;
    border-radius: 50%;
    background: var(--ink);
  }
  .card--front .wordmark {
    font-size: 34px;
    left: 50%; top: 50%;
    transform: translate(-50%, -50%);
  }
  .card--back .wordmark {
    font-size: 30px;
    left: 402px; top: 188px;
  }

  .contact {
    position: absolute;
    left: 66px; top: 68px;
  }
  .contact__name {
    font-size: 24px;
    font-weight: 700;
    color: var(--name-grey);
  }
  .contact__title {
    font-size: 16px;
    margin-top: 6px;
  }
  .contact__list {
    list-style: none;
    margin-top: 52px;
    font-size: 18px;
  }
  .contact__list li {
    display: flex;
    align-items: center;
    height: 27px;
  }
  .contact__icon {
    width: 18px; height: 14px;
    margin-right: 18px;
    fill: var(--icon-grey);
    stroke: var(--icon-grey);
  }
  .contact__address {
    font-size: 18px;
    line-height: 27px;
  }
  .card__band {
    position: absolute;
    left: 0; right: 0; bottom: 0;
    height: 26px;
    background: linear-gradient(90deg, var(--band-teal), var(--band-green));
  }
</style>
</head>
<body>
  <section class="card card--front" aria-label="Card front">
    <div class="wordmark"><span class="wordmark__dot"></span>FROSTLEAF SPA</div>
  </section>

  <section class="card card--back" aria-label="Card back">
    <div class="contact">
      <p class="contact__name">Your Long Name</p>
      <p class="contact__title">Your Title</p>
      <ul class="contact__list">
        <li>
          <svg class="contact__icon" viewBox="0 0 18 14" aria-hidden="true"><path stroke="none" d="M2 4c0-2 3-3 7-3s7 1 7 3v2h-4V4H6v2H2z"/><rect stroke="none" x="4" y="7" width="10" height="6" rx="1"/></svg>
          (555) 014-2290
        </li>
        <li>
          <svg class="contact__icon" viewBox="0 0 18 14" aria-hidden="true"><rect x="1.5" y="2" width="15" height="10" fill="none" stroke-width="1.6"/><path d="M1.5 2l7.5 6 7.5-6" fill="none" stroke-width="1.6"/></svg>
          info@frostleafspa-example.com
        </li>
        <li>
          <svg class="contact__icon" viewBox="0 0 18 14" aria-hidden="true"><circle cx="9" cy="7" r="6" fill="none" stroke-width="1.4"/><ellipse cx="9" cy="7" rx="2.6" ry="6" fill="none" stroke-width="1.2"/><path d="M3 7h12" stroke-width="1.2"/></svg>
          www.frostleafspa-example.com
        </li>
      </ul>
      <p class="contact__address">2250 Birchwood Lane Suite 140<br>Maple Grove, IL 60099</p>
    </div>
    <div class="wordmark"><span class="wordmark__dot"></span>FROSTLEAF SPA</div>
    <div class="card__band"></div>
  </section>
</body>
</html>
```